Plakat-Design für Förderverein einer Feuerwehr
Zielgruppe
Wir sind ein Förderverein einer Feuerwehr und suchen ein modernes Design für unser Banner und Plakat für das Maifest
Aufgabenstellung
Das Banner soll die Maße von 2x1m haben und das Plakat soll das Format A3 haben. Der Textinhalt soll so bleiben.

```html
<!DOCTYPE html>
<html lang="de">
<head>
<meta charset="utf-8">
<title>Maifest – Banner und Plakat</title>
<link href="https://fonts.googleapis.com/css2?family=Montserrat:ital,wght@0,500;0,700;0,800;0,900;1,500;1,700;1,800;1,900&display=swap" rel="stylesheet">
<style>
  :root {
    --red: #ed1c24;
    --navy: #2b3a67;
    --yellow: #fdc82f;
    --white: #ffffff;
    --ink: #1a1a1a;
    --stage: #d4d4d4;
    --smoke-light: #c9ccd0;
    --smoke-dark: #6f747c;
    --gear: #b39a3e;
  }
  * { margin: 0; padding: 0; box-sizing: border-box; }
  html, body { width: 935px; height: 1200px; overflow: hidden; }
  body {
    background: var(--stage);
    font-family: "Montserrat", Arial, sans-serif;
    position: relative;
  }
  .piece { position: absolute; overflow: hidden; background: var(--white); }
  .banner { left: 46px; top: 71px; width: 843px; height: 422px; }
  .poster { left: 258px; top: 520px; width: 420px; height: 607px; }
  .shapes { position: absolute; inset: 0; width: 100%; height: 100%; }
  .abs { position: absolute; white-space: nowrap; line-height: 1; }

  .brand {
    color: var(--white); font-weight: 800; font-style: normal;
    display: flex; align-items: center; gap: 8px;
  }
  .brand-square { background: var(--white); display: inline-block; }

  .emblem {
    position: absolute; border-radius: 50%;
    background: var(--white);
    display: flex; align-items: center; justify-content: center;
  }
  .emblem-inner {
    border-radius: 50%;
    border: 4px solid var(--ink);
    background: radial-gradient(circle, #8a8a8a 0%, #3a3a3a 100%);
  }

  .club { color: var(--navy); font-weight: 800; font-style: italic; }
  .org { color: var(--red); font-weight: 900; font-style: italic; letter-spacing: 0.5px; }
  .unit-pill {
    position: absolute; background: var(--navy); color: var(--white);
    font-weight: 700; font-style: italic;
    border-radius: 12px 4px 12px 4px;
    box-shadow: 4px 4px 0 #b8bcc6;
    display: flex; align-items: center; justify-content: center;
  }
  .url { color: var(--red); font-weight: 800; font-style: italic; }
  .day { color: var(--yellow); font-weight: 900; font-style: italic; }
  .date { color: var(--white); font-weight: 800; }
  .time-pill {
    position: absolute; background: var(--red); color: var(--white);
    font-weight: 700; border-radius: 12px;
    box-shadow: 3px 3px 0 var(--ink);
    display: flex; align-items: center; justify-content: center;
  }
  .festname {
    color: var(--red); font-weight: 900; font-style: italic; letter-spacing: -1px;
    text-shadow:
      -2px -2px 0 var(--white), 2px -2px 0 var(--white),
      -2px 2px 0 var(--white), 2px 2px 0 var(--white),
      0 -3px 0 var(--white), 0 3px 0 var(--white),
      -3px 0 0 var(--white), 3px 0 0 var(--white),
      5px 5px 0 var(--ink);
  }

  .venue-badge {
    color: var(--white); font-weight: 800; font-style: italic;
    text-align: center; line-height: 1.15; white-space: normal;
  }
  .program { color: var(--white); font-weight: 800; font-style: italic; }
  .program-list { list-style: none; }
  .program-list li { position: relative; padding-left: 14px; margin-bottom: 13px; line-height: 1.15; }
  .tick { position: absolute; left: 0; top: 1px; width: 8px; height: 8px; }
  .catering-note { color: var(--white); font-weight: 500; font-style: italic; line-height: 1.4; white-space: normal; }
  .offer { color: var(--white); font-weight: 900; font-style: italic; text-align: right; }
  .offer-url { color: var(--yellow); font-weight: 800; font-style: italic; }
</style>
</head>
<body>

<!-- Banner 2 x 1 m -->
<section class="piece banner">
  <svg class="shapes" viewBox="0 0 843 422" preserveAspectRatio="none" aria-hidden="true">
    <defs>
      <linearGradient id="banner-photo" x1="0" y1="0" x2="1" y2="0">
        <stop offset="0" stop-color="var(--smoke-light)"/>
        <stop offset="0.35" stop-color="var(--smoke-dark)"/>
        <stop offset="0.7" stop-color="var(--gear)"/>
        <stop offset="1" stop-color="#7d6a2a"/>
      </linearGradient>
    </defs>
    <path d="M330 0 H843 V225 C700 195 520 172 400 178 C385 165 360 140 330 120 Z" fill="url(#banner-photo)" role="img" aria-label="Foto: Feuerwehrleute mit Atemschutz im Rauch"/>
    <path d="M0 0 H330 C320 40 340 80 330 120 C320 150 300 155 280 153 C180 148 80 130 0 117 Z" fill="var(--red)"/>
    <path d="M400 178 C520 170 700 190 843 215 V422 H0 V388 C120 400 300 402 400 400 C440 396 440 360 420 320 C400 280 380 240 395 205 C398 190 400 180 400 178 Z" fill="var(--navy)"/>
  </svg>

  <div class="abs brand" style="left:51px; top:56px; font-size:19px;">
    <span>Feuerwehr Talstadt</span><span class="brand-square" style="width:15px;height:15px;"></span>
  </div>

  <div class="emblem" style="left:280px; top:41px; width:154px; height:154px;">
    <div class="emblem-inner" role="img" aria-label="Emblem der Feuerwehr" style="width:136px;height:136px;"></div>
  </div>

  <div class="abs club" style="left:53px; top:170px; font-size:29px;">Forderverein</div>
  <div class="abs org" style="left:44px; top:212px; font-size:44px;">FREIWILLIGE</div>
  <div class="abs org" style="left:44px; top:258px; font-size:44px;">FEUERWEHR</div>
  <div class="unit-pill" style="left:40px; top:309px; width:335px; height:37px; font-size:23px;">Löschzug Lindenhöhe</div>
  <div class="abs url" style="left:70px; top:360px; font-size:15px;">www.feuerwehr-talstadt.de</div>

  <div class="abs day" style="left:463px; top:198px; font-size:52px;">Samstag</div>
  <div class="abs date" style="left:461px; top:266px; font-size:36px;">26.5.24</div>
  <div class="time-pill" style="left:626px; top:262px; width:176px; height:42px; font-size:30px;">ab 12 Uhr</div>
  <div class="abs festname" style="left:456px; top:312px; font-size:80px;">Maifest</div>
</section>

<!-- Plakat A3 -->
<section class="piece poster">
  <svg class="shapes" viewBox="0 0 420 607" preserveAspectRatio="none" aria-hidden="true">
    <defs>
      <linearGradient id="poster-photo" x1="0" y1="0" x2="1" y2="0">
        <stop offset="0" stop-color="var(--smoke-light)"/>
        <stop offset="0.4" stop-color="var(--smoke-dark)"/>
        <stop offset="0.75" stop-color="var(--gear)"/>
        <stop offset="1" stop-color="#7d6a2a"/>
      </linearGradient>
      <polygon id="burst" points="0,-56 12,-50 24,-53 32,-42 45,-38 46,-25 56,-15 51,-3 56,9 48,19 49,33 37,39 31,51 18,50 6,57 -6,51 -19,54 -27,43 -40,40 -42,27 -53,19 -49,7 -56,-5 -48,-15 -49,-29 -37,-35 -31,-47 -18,-47 -7,-55"/>
    </defs>
    <rect x="0" y="0" width="420" height="310" fill="url(#poster-photo)" role="img" aria-label="Foto: Feuerwehrleute mit Atemschutz im Rauch"/>
    <path d="M0 0 H198 C206 30 214 60 205 80 C200 88 190 88 170 88 C110 86 50 80 0 70 Z" fill="var(--red)"/>
    <path d="M0 170 C100 158 180 165 250 180 C280 186 300 200 290 230 C285 260 320 280 420 300 V607 H0 Z" fill="var(--white)"/>
    <path d="M0 413 C60 360 150 320 260 306 C320 299 380 300 420 303 V607 H0 Z" fill="var(--navy)"/>
    <path d="M160 486 C250 480 340 484 420 500 V607 H170 C180 580 160 560 150 530 C140 505 145 488 160 486 Z" fill="var(--red)"/>
    <use href="#burst" transform="translate(76 381)" fill="var(--white)"/>
    <use href="#burst" transform="translate(76 381) scale(0.92)" fill="var(--red)"/>
  </svg>

  <div class="abs brand" style="left:31px; top:32px; font-size:16px;">
    <span>Feuerwehr Talstadt</span><span class="brand-square" style="width:12px;height:12px;"></span>
  </div>

  <div class="emblem" style="left:270px; top:180px; width:108px; height:108px;">
    <div class="emblem-inner" role="img" aria-label="Emblem der Feuerwehr" style="width:98px;height:98px;"></div>
  </div>

  <div class="abs club" style="left:33px; top:186px; font-size:21px;">Forderverein</div>
  <div class="abs org" style="left:26px; top:211px; font-size:29px;">FREIWILLIGE</div>
  <div class="abs org" style="left:26px; top:243px; font-size:29px;">FEUERWEHR</div>
  <div class="unit-pill" style="left:24px; top:275px; width:228px; height:26px; font-size:16px; border-radius:9px 3px 9px 3px; box-shadow:3px 3px 0 #b8bcc6;">Löschzug Lindenhöhe</div>

  <div class="abs venue-badge" style="left:26px; top:355px; width:100px; font-size:10px;">Feuerwehr<br>gerätehaus<br>Lindenhöher<br>Straße</div>

  <div class="abs day" style="left:155px; top:342px; font-size:35px;">Samstag</div>
  <div class="abs date" style="left:154px; top:388px; font-size:25px;">26.5.24</div>
  <div class="time-pill" style="left:269px; top:386px; width:122px; height:28px; font-size:21px; border-radius:8px;">ab 12 Uhr</div>
  <div class="abs festname" style="left:150px; top:428px; font-size:53px;">Maifest</div>

  <div class="abs program" style="left:23px; top:455px; font-size:10.5px;">Tag der offenen Tür</div>
  <ul class="abs program program-list" style="left:23px; top:475px; font-size:10px; white-space:normal; width:110px;">
    <li><svg class="tick" viewBox="0 0 8 8"><circle cx="4" cy="4" r="4" fill="var(--red)"/><path d="M2 4.2 L3.5 5.6 L6 2.6" stroke="var(--white)" stroke-width="1.2" fill="none"/></svg>Ausstellung der Fahrzeuge</li>
    <li><svg class="tick" viewBox="0 0 8 8"><circle cx="4" cy="4" r="4" fill="var(--red)"/><path d="M2 4.2 L3.5 5.6 L6 2.6" stroke="var(--white)" stroke-width="1.2" fill="none"/></svg>Belustigung der kleinen mit Hupfburg etc.</li>
  </ul>
  <div class="abs catering-note" style="left:37px; top:560px; width:110px; font-size:8.5px;">Wir versorgen Sie den gesamten Tag mit</div>

  <div class="abs offer" style="right:32px; top:503px; font-size:24px;">Softdrinks</div>
  <div class="abs offer" style="right:32px; top:530px; font-size:24px;">Bier vom Fass</div>
  <div class="abs offer" style="right:32px; top:562px; font-size:12.5px;">Spezialitaten frisch vom Grill</div>
  <div class="abs offer-url" style="right:32px; top:582px; font-size:10.5px;">www.feuerwehr-talstadt.de</div>
</section>

</body>
</html>
```